CHIP BAG AND LOGO DESIGN - A salty snack that is focused on taste and texture

I need a logo and label design for our new brand "Vexamba". A salty snack that brings corn tortilla with extreme spices to excite the taste. First Flavor will be 'Trueno Pimienta and Kiwi'. Looking for a label design and a logo design for the Brand 'Vexamba'. This brand will have multiple types of snacks and all with different flavors and heat levels.

Target Market(s)

10- 25 year old

Industry/Entity Type

Salty Snacks

Font styles to use
Sans Serif
Other font styles liked:
• Arial, Bauhaus 93, Berlin Sans FB Demi, Cooper Black

Colors
59FF00
82FF00
B8FF75
E3FFCB
F4FFEA
FFF300
FFF600
FEFA6F
FFFEC7
FFFEE8
FFC000
F8CF3A
FAE287
FDF2CF
FEFAEE
F0912C
F2A743
F7CA91
FBE8D2
FDF5EE
EE7325
F08F49
F5BC92
FAE3D3
FDF4ED
EB3D1F
EC4F4E
F09395
F8D3D4
FCEDEE

Requirements
Must have
• Colors and design that pops, need the bags to jump off the shelf in a sea of competitors. I gave an example of Walrus Flax, I appreciate the artwork and design they did to differentiate their brand from others and appeal to the 10-25 demographics.
Nice to have
• Abstract / Cartoon like characteristics that speak of a south of the border recipe and origin. I would like to have in subtle grey or black background design much like the Aztec calendar that fills the space on a bag and/or a variation of that kind of design. In the front I'd like a character (maybe a warrior) of the same fashion. The logo (also being designed - "VEXAMBA") carefully blended into the artwork. Bold, Loud, jumps off the shelf with bright colors and graphics.
Should not have
• bland, boring, blah colors and designs. Should be fun and loud.

```html
<!DOCTYPE html>
<html lang="en">
<head>
<meta charset="utf-8">
<title>Vexamba – Trueno Pimienta and Kiwi</title>
<link rel="stylesheet" href="https://fonts.googleapis.com/css2?family=Fredoka:wght@700&family=Londrina+Solid:wght@900&display=swap">
<style>
  :root {
    --page: #ffffff;
    --bag-red: #cf352b;
    --bag-red-light: #e8685c;
    --bag-coral: #f07560;
    --bag-red-dark: #5e0a0c;
    --seal-red: #a9221f;
    --seal-red-light: #c2332b;
    --gold: #f5cf4f;
    --gold-deep: #e6a93a;
    --band-red: #d0463a;
    --logo-yellow: #f6cf4a;
    --emblem-gold: #f7cf45;
    --emblem-orange: #ee8a3c;
    --emblem-red: #c7362e;
    --chip: #efd49a;
    --chip-shade: #d8ae68;
    --flavor-grey: #d6d6da;
    --flavor-grey-dark: #a9a9b0;
  }
  * { box-sizing: border-box; margin: 0; padding: 0; }
  html, body {
    width: 1200px;
    height: 960px;
    overflow: hidden;
    background: var(--page);
  }
  .canvas { position: relative; width: 1200px; height: 960px; }

  .bag {
    position: absolute;
    left: 316px;
    top: 136px;
    width: 586px;
    height: 700px;
    background: linear-gradient(180deg, var(--bag-red-light) 0%, var(--bag-red) 50%, #b8271f 72%, var(--bag-red-dark) 100%);
    overflow: hidden;
  }
  .seal {
    position: absolute;
    left: 0;
    width: 100%;
    background: repeating-linear-gradient(180deg, var(--seal-red) 0 4px, var(--seal-red-light) 4px 7px);
  }
  .seal--top { top: 0; height: 34px; }
  .seal--bottom { bottom: 0; height: 40px; }

  .glow-band {
    position: absolute;
    left: 0;
    top: 250px;
    width: 100%;
    height: 330px;
    background: linear-gradient(180deg, rgba(240,117,96,0) 0%, rgba(244,128,100,0.75) 20%, rgba(232,92,68,0.6) 75%, rgba(232,92,68,0) 100%);
  }

  .pattern-band { position: absolute; left: 34px; right: 34px; }
  .pattern-band--zigzag {
    top: 92px;
    height: 40px;
    border-top: 3px solid var(--gold);
    border-bottom: 3px solid var(--gold);
    background: linear-gradient(180deg, var(--band-red) 0%, var(--gold-deep) 55%, var(--gold) 100%);
  }
  .pattern-band--key-top {
    top: 137px;
    height: 24px;
    border: 3px solid var(--gold);
    background: linear-gradient(90deg, var(--gold-deep), var(--gold) 50%, var(--gold-deep));
  }
  .pattern-band--key-bottom {
    bottom: 6px;
    height: 26px;
    left: 8px;
    right: 8px;
    border: 3px solid var(--gold);
    background: linear-gradient(90deg, var(--gold-deep), var(--gold) 50%, var(--gold-deep));
  }

  .brand-name {
    position: absolute;
    top: 178px;
    left: 0;
    width: 100%;
    text-align: center;
    font-family: "Fredoka", sans-serif;
    font-weight: 700;
    font-size: 92px;
    line-height: 1;
    letter-spacing: 1px;
    color: var(--logo-yellow);
  }

  .emblem {
    position: absolute;
    left: 150px;
    top: 250px;
    width: 286px;
    height: 286px;
    border-radius: 50%;
    background: radial-gradient(circle, var(--emblem-orange) 0%, var(--emblem-gold) 30%, var(--emblem-red) 44%, var(--emblem-orange) 52%, var(--emblem-gold) 64%, rgba(247,207,69,0.55) 76%, rgba(247,207,69,0) 100%);
  }

  .chip {
    position: absolute;
    background: radial-gradient(ellipse at 40% 40%, var(--chip) 0%, var(--chip-shade) 100%);
    border-radius: 50%;
  }
  .chip--one { left: 100px; top: 320px; width: 172px; height: 32px; transform: rotate(24deg); }
  .chip--two { left: 352px; top: 404px; width: 154px; height: 64px; transform: rotate(-6deg); }
  .chip--three { left: 360px; top: 500px; width: 144px; height: 30px; transform: rotate(22deg); }

  .flavor {
    position: absolute;
    top: 562px;
    left: 0;
    width: 100%;
    text-align: center;
    font-family: "Londrina Solid", sans-serif;
    font-weight: 900;
    font-size: 48px;
    line-height: 0.88;
    color: var(--flavor-grey);
  }
</style>
</head>
<body>
<main class="canvas">
  <section class="bag" aria-label="Vexamba snack bag front">
    <div class="seal seal--top"></div>
    <div class="glow-band"></div>

    <div class="pattern-band pattern-band--zigzag" role="img" aria-label="Gold zigzag and dot border pattern"></div>
    <div class="pattern-band pattern-band--key-top" role="img" aria-label="Gold step-fret key border pattern"></div>

    <h1 class="brand-name">VEXAMBA</h1>

    <div class="emblem" role="img" aria-label="Golden sun-stone emblem with warrior motif"></div>

    <div class="chip chip--one" role="img" aria-label="Tortilla chip"></div>
    <div class="chip chip--two" role="img" aria-label="Tortilla chip"></div>
    <div class="chip chip--three" role="img" aria-label="Tortilla chip"></div>

    <p class="flavor">Trueno Pimienta<br>and Kiwi</p>

    <div class="seal seal--bottom"></div>
    <div class="pattern-band pattern-band--key-bottom" role="img" aria-label="Gold step-fret key border pattern"></div>
  </section>
</main>
</body>
</html>
```